New Bicycle shop business card

Hi!
I'm looking for a business card for my new proffesional bike mechanics shop. This shop is only for fixing broken bikes and not selling bikes.
Peferbly a modern and sleek and modern design.
Colors: black, grey, red, white
Information:
Name: Velowerkplaats Martens
Shop owner: Bart Martens & Sofie Vanhulle
Website: www.velowerkplaats-martens.be
Email: info@velowerkplaats-martens.be
Phone number: +32471936208
Street adres: Molenweg 57
9470 Keerdonk
Slogan/shop information: Herstellingen van alle merken.
Logo: see files.
Target Market(s)
People who seek a mechanic to fix or upgrade their bikes.
Contact Information for Business Card
Information:
Website: info@velowerkplaats-martens.be
9470 Keerdonk
Logo: see files.

```html
<!DOCTYPE html>
<html lang="nl">
<head>
<meta charset="utf-8">
<title>Velowerkplaats Martens – visitekaartje</title>
<link href="https://fonts.googleapis.com/css2?family=Roboto:wght@400;500;700;900&display=swap" rel="stylesheet">
<style>
  :root {
    --bg: #3a3a3c;
    --card: #1f1f21;
    --card-decor: #262629;
    --red: #e02d3c;
    --grey: #a7a9ac;
    --white: #ffffff;
    --muted: #d9d9db;
    --emboss: #48484c;
  }
  * { margin: 0; padding: 0; box-sizing: border-box; }
  html, body { width: 799px; height: 1200px; overflow: hidden; }
  body {
    background: var(--bg);
    font-family: "Roboto", Arial, sans-serif;
    position: relative;
  }
  .card {
    position: absolute;
    left: 90px;
    width: 620px;
    height: 380px;
    border-radius: 28px;
    background: var(--card);
    overflow: hidden;
    box-shadow: 0 18px 40px rgba(0,0,0,.45);
  }
  .card--front { top: 120px; }
  .card--back { top: 680px; }

  /* front */
  .front-mark {
    position: absolute;
    inset: 0;
    display: flex;
    align-items: center;
    justify-content: center;
    gap: 16px;
  }
  .front-mark__dot {
    width: 22px; height: 22px; border-radius: 50%;
    background: var(--emboss);
  }
  .front-mark__name {
    font-weight: 700;
    font-size: 28px;
    letter-spacing: 2px;
    text-transform: uppercase;
    color: var(--emboss);
  }

  /* back */
  .back-decor {
    position: absolute;
    right: -60px; top: 90px;
    width: 340px; height: 340px;
    border-radius: 50%;
    background: var(--card-decor);
  }
  .brand {
    position: absolute;
    left: 40px; top: 40px;
    display: flex; align-items: center; gap: 14px;
  }
  .brand__dot { width: 26px; height: 26px; border-radius: 50%; background: var(--red); }
  .brand__name {
    font-weight: 700; font-size: 26px; letter-spacing: 1.5px;
    text-transform: uppercase; color: var(--white);
  }
  .person { position: absolute; left: 40px; top: 130px; }
  .person__name {
    font-weight: 700; font-size: 24px; text-transform: uppercase;
    color: var(--red); letter-spacing: .5px;
  }
  .person__role { font-size: 14px; color: var(--muted); margin-top: 2px; }
  .address { position: absolute; left: 40px; top: 205px; font-size: 16px; line-height: 1.4; color: var(--white); }
  .contact {
    position: absolute; left: 320px; top: 200px;
    list-style: none; font-size: 16px; color: var(--white);
  }
  .contact li { display: flex; align-items: center; gap: 12px; height: 26px; }
  .contact svg { width: 14px; height: 14px; flex: none; }
  .icon-fill { fill: var(--red); }
  .icon-line { fill: none; stroke: var(--red); stroke-width: 2; }
  .bands { position: absolute; left: 0; bottom: 0; width: 620px; height: 70px; }
  .slogan {
    position: absolute; right: 40px; bottom: 20px;
    font-size: 18px; font-weight: 400; color: var(--white);
  }
</style>
</head>
<body>

<section class="card card--front" aria-label="Voorkant visitekaartje">
  <div class="front-mark">
    <span class="front-mark__dot"></span>
    <span class="front-mark__name">Velowerkplaats Martens</span>
  </div>
</section>

<section class="card card--back" aria-label="Achterkant visitekaartje">
  <div class="back-decor"></div>

  <div class="brand">
    <span class="brand__dot"></span>
    <span class="brand__name">Velowerkplaats Martens</span>
  </div>

  <div class="person">
    <p class="person__name">Sofie Vanhulle</p>
    <p class="person__role">Owner</p>
  </div>

  <p class="address">Molenweg 57<br>9470 Keerdonk</p>

  <ul class="contact">
    <li>
      <svg viewBox="0 0 24 24" aria-hidden="true"><path class="icon-fill" d="M6.6 10.8a15 15 0 0 0 6.6 6.6l2.2-2.2a1 1 0 0 1 1-.25 11.4 11.4 0 0 0 3.6.57 1 1 0 0 1 1 1V20a1 1 0 0 1-1 1A17 17 0 0 1 3 4a1 1 0 0 1 1-1h3.5a1 1 0 0 1 1 1c0 1.25.2 2.45.57 3.6a1 1 0 0 1-.25 1z"/></svg>
      +32471936208
    </li>
    <li>
      <svg viewBox="0 0 24 24" aria-hidden="true"><rect class="icon-line" x="3" y="5" width="18" height="14"/><path class="icon-line" d="M3 5l9 7 9-7"/></svg>
      www.velowerkplaats-martens.be
    </li>
    <li>
      <svg viewBox="0 0 24 24" aria-hidden="true"><circle class="icon-line" cx="12" cy="12" r="9"/><path class="icon-line" d="M3 12h18M12 3c3 3 3 15 0 18M12 3c-3 3-3 15 0 18"/></svg>
      info@velowerkplaats-martens.be
    </li>
  </ul>

  <svg class="bands" viewBox="0 0 620 70" preserveAspectRatio="none" aria-hidden="true">
    <polygon points="0,50 300,50 300,70 0,70" fill="#a7a9ac"/>
    <path d="M330 0 H620 V70 H280 Z" fill="#e02d3c"/>
  </svg>
  <p class="slogan">Herstellingen van alle merken</p>
</section>

</body>
</html>
```